Cover for Every door Opens Where Every Door Opens

Book Cover Request
Format: Print and electronic (Quillmart)
Book Title: Every Door Opens Where Every Door Opens: Practical Roadmap for Courage and Progress
Author: R.K. Vantreel
Description: This self-help book, written by me, a self-proclaimed nobody, is filled with actionable insights and proven strategies that can help anyone. It combines humor with a serious undertone to deliver practical advice without the typical "self-helpy" vibe.
Catchphrase for the Cover: "Go from Oh Shit to Crushing It!" (or something similar)
Style: I want the cover to reflect my personality—funny, yet serious when needed. I'm open to suggestions and would love to see a design that captures the essence of the book without being too typical of the self-help genre.
Additional Information: I've attached a rough draft of the Quillmart description for more context.
Thank you for your help!
Target Market(s)
Anyone. but id say over 25
Requirements
Nice to have
- Honestly im really at a loss. Im hoping the description will help guide you. I gues i would like it to satand out of course. Be diffrent....but i know how crazy that sounds because everyone wants that. Just give me soem ideas!

```html
<!DOCTYPE html>
<html lang="en">
<head>
<meta charset="utf-8">
<title>Every Door Opens Where Every Door Opens — Cover Options</title>
<link href="https://fonts.googleapis.com/css2?family=Anton&family=Bebas+Neue&display=swap" rel="stylesheet">
<style>
  :root {
    --ink: #0a0a0b;
    --paper: #ffffff;
    --gold: #fdbf12;
    --gold-shade: #d99f0c;
    --leaf: #5fbc46;
    --leaf-shade: #4b9a37;
  }
  html, body {
    margin: 0;
    padding: 0;
    width: 1200px;
    height: 775px;
    overflow: hidden;
    background: var(--paper);
  }
  .cover {
    position: absolute;
    top: 78px;
    width: 396px;
    height: 614px;
    filter: drop-shadow(12px 14px 10px rgba(0, 0, 0, 0.45));
  }
  .cover--gold { left: 149px; --accent: var(--gold); --accent-shade: var(--gold-shade); }
  .cover--leaf { left: 645px; --accent: var(--leaf); --accent-shade: var(--leaf-shade); }

  .frame-base { fill: var(--ink); }
  .frame-rule { fill: none; stroke: var(--accent); stroke-width: 6; }
  .panel { fill: var(--accent); }
  .ink-shape { fill: var(--ink); }
  .art-area { fill: var(--accent-shade); }

  .author { font-family: "Bebas Neue", sans-serif; font-size: 28px; fill: var(--accent); }
  .title-top { font-family: "Anton", sans-serif; font-size: 70px; fill: var(--ink); }
  .title-main { font-family: "Anton", sans-serif; font-size: 84px; fill: var(--ink); }
  .title-tail { font-family: "Bebas Neue", sans-serif; font-size: 33px; fill: var(--ink); }
  .subtitle { font-family: "Bebas Neue", sans-serif; fill: var(--accent); }
  .subtitle--sm { font-size: 43px; }
  .subtitle--md { font-size: 53px; }
  .subtitle--lg { font-size: 68px; }
  .tagline { font-family: "Bebas Neue", sans-serif; font-size: 34px; fill: var(--accent); }
  .tag-icon { fill: var(--accent); }
</style>
</head>
<body>

<svg class="cover cover--gold" viewBox="0 0 396 614" aria-label="Book cover, gold edition">
  <rect class="frame-base" x="0" y="0" width="396" height="614"/>
  <rect class="frame-rule" x="14" y="14" width="368" height="586"/>
  <rect class="panel" x="28.5" y="28.5" width="339" height="462"/>

  <path class="ink-shape" d="M131,28.5 L265,28.5 L251,60.5 L146,60.5 Z"/>
  <text class="author" x="198" y="56" text-anchor="middle" textLength="92" lengthAdjust="spacingAndGlyphs">R.K. VANTREEL</text>

  <text class="title-top" x="196" y="149.5" text-anchor="middle" textLength="178" lengthAdjust="spacingAndGlyphs">EVERY DOOR</text>
  <text class="title-main" x="196" y="217" text-anchor="middle" textLength="227" lengthAdjust="spacingAndGlyphs">OPENS</text>
  <text class="title-tail" x="196" y="244.5" text-anchor="middle" textLength="225" lengthAdjust="spacingAndGlyphs">WHERE EVERY DOOR OPENS</text>

  <g role="img" aria-label="Illustration: a hamster running in an exercise wheel on a stand">
    <circle class="art-area" cx="197" cy="324" r="72"/>
  </g>

  <path class="ink-shape" d="M28.5,490 L131,415 C158,401 178,398.5 197,398.5 C216,398.5 240,402 266,417 L367.5,491 L367.5,500 L28.5,500 Z"/>

  <g transform="translate(204.5,444.5) skewX(-12)">
    <text class="subtitle subtitle--sm" x="0" y="0" text-anchor="middle" textLength="103" lengthAdjust="spacingAndGlyphs">PRACTICAL</text>
  </g>
  <g transform="translate(202,488) skewX(-12)">
    <text class="subtitle subtitle--md" x="0" y="0" text-anchor="middle" textLength="178" lengthAdjust="spacingAndGlyphs">ROADMAP FOR</text>
  </g>
  <g transform="translate(199,542) skewX(-12)">
    <text class="subtitle subtitle--lg" x="0" y="0" text-anchor="middle" textLength="314" lengthAdjust="spacingAndGlyphs">COURAGE AND PROGRESS</text>
  </g>

  <text class="tagline" x="35" y="578.5" textLength="120" lengthAdjust="spacingAndGlyphs">GO FROM OH</text>
  <path class="tag-icon" role="img" aria-label="Small poop emoji icon" d="M163.5,578.5 C162,570 168,566 171,566 C170,559 176,555 179,553 C182,555 188,559 187,566 C190,566 196,570 194.5,578.5 Z"/>
  <text class="tagline" x="201" y="578.5" textLength="159" lengthAdjust="spacingAndGlyphs">TO CRUSHING IT!</text>
</svg>

<svg class="cover cover--leaf" viewBox="0 0 396 614" aria-label="Book cover, green edition">
  <rect class="frame-base" x="0" y="0" width="396" height="614"/>
  <rect class="frame-rule" x="14" y="14" width="368" height="586"/>
  <rect class="panel" x="28.5" y="28.5" width="339" height="462"/>

  <path class="ink-shape" d="M131,28.5 L265,28.5 L251,60.5 L146,60.5 Z"/>
  <text class="author" x="198" y="56" text-anchor="middle" textLength="92" lengthAdjust="spacingAndGlyphs">R.K. VANTREEL</text>

  <text class="title-top" x="196" y="149.5" text-anchor="middle" textLength="178" lengthAdjust="spacingAndGlyphs">EVERY DOOR</text>
  <text class="title-main" x="196" y="217" text-anchor="middle" textLength="227" lengthAdjust="spacingAndGlyphs">OPENS</text>
  <text class="title-tail" x="196" y="244.5" text-anchor="middle" textLength="225" lengthAdjust="spacingAndGlyphs">WHERE EVERY DOOR OPENS</text>

  <g role="img" aria-label="Illustration: a hamster running in an exercise wheel on a stand">
    <circle class="art-area" cx="197" cy="324" r="72"/>
  </g>

  <path class="ink-shape" d="M28.5,490 L131,415 C158,401 178,398.5 197,398.5 C216,398.5 240,402 266,417 L367.5,491 L367.5,500 L28.5,500 Z"/>

  <g transform="translate(204.5,444.5) skewX(-12)">
    <text class="subtitle subtitle--sm" x="0" y="0" text-anchor="middle" textLength="103" lengthAdjust="spacingAndGlyphs">PRACTICAL</text>
  </g>
  <g transform="translate(202,488) skewX(-12)">
    <text class="subtitle subtitle--md" x="0" y="0" text-anchor="middle" textLength="178" lengthAdjust="spacingAndGlyphs">ROADMAP FOR</text>
  </g>
  <g transform="translate(199,542) skewX(-12)">
    <text class="subtitle subtitle--lg" x="0" y="0" text-anchor="middle" textLength="314" lengthAdjust="spacingAndGlyphs">COURAGE AND PROGRESS</text>
  </g>

  <text class="tagline" x="35" y="578.5" textLength="120" lengthAdjust="spacingAndGlyphs">GO FROM OH</text>
  <path class="tag-icon" role="img" aria-label="Small poop emoji icon" d="M163.5,578.5 C162,570 168,566 171,566 C170,559 176,555 179,553 C182,555 188,559 187,566 C190,566 196,570 194.5,578.5 Z"/>
  <text class="tagline" x="201" y="578.5" textLength="159" lengthAdjust="spacingAndGlyphs">TO CRUSHING IT!</text>
</svg>

</body>
</html>
```